Medical software helping patients with dry eye disease needs a business card

We have a logo we just need a design for a business card for a Canadian company called LOV: Dry Eye. We use AI technology to assist optometrists in properly diagnosing patients with dry eye disease reducing wait times in doctors offices and accuracy of diagnosis as well as identifying key possible indicators and tailored treatment plans. The final design should be clean and medical looking. Our mission is to help patients and our logo using blues and whites.

```html
<!DOCTYPE html>
<html lang="en">
<head>
<meta charset="utf-8">
<title>LOV: Dry Eye — Business Card</title>
<link rel="stylesheet" href="https://fonts.googleapis.com/css2?family=Montserrat:wght@700;800&family=Mulish:wght@400;500&display=swap">
<style>
  :root {
    --backdrop: #cfd3d4;
    --card: #121315;
    --blue: #1ea7e1;
    --white: #f4f5f6;
    --muted: #d9dcde;
  }
  * { box-sizing: border-box; margin: 0; padding: 0; }
  html, body { width: 1200px; height: 1028px; overflow: hidden; }
  body {
    background: var(--backdrop);
    display: flex;
    flex-direction: column;
    align-items: center;
    justify-content: center;
    gap: 56px;
    font-family: "Mulish", sans-serif;
  }
  .card {
    position: relative;
    width: 760px;
    height: 434px;
    background: var(--card);
    border-bottom: 5px solid var(--blue);
    box-shadow: 0 14px 30px rgba(0,0,0,0.25);
  }
  .brand {
    position: absolute;
    display: flex;
    align-items: center;
    gap: 18px;
    font-family: "Montserrat", sans-serif;
    font-weight: 800;
    color: var(--blue);
    white-space: nowrap;
  }
  .brand-dot {
    border-radius: 50%;
    background: var(--blue);
    flex: none;
  }
  .card-front .brand { left: 50%; top: 50%; transform: translate(-50%, -50%); font-size: 68px; }
  .card-front .brand-dot { width: 64px; height: 64px; }

  .card-back .brand { right: 48px; top: 86px; font-size: 42px; gap: 12px; }
  .card-back .brand-dot { width: 40px; height: 40px; }

  .holder { position: absolute; left: 52px; top: 60px; }
  .holder-name {
    font-family: "Montserrat", sans-serif;
    font-weight: 800;
    font-size: 34px;
    letter-spacing: 0.5px;
    color: var(--blue);
    text-transform: uppercase;
  }
  .holder-role { font-size: 19px; color: var(--muted); margin-top: 2px; }

  .rule {
    position: absolute;
    left: 52px; right: 48px; top: 168px;
    height: 1.5px;
    background: var(--blue);
  }
  .contact-list {
    position: absolute;
    left: 52px; top: 198px;
    list-style: none;
    font-size: 21px;
    color: var(--white);
    line-height: 1.75;
  }
  .contact-list li { display: flex; align-items: center; gap: 12px; }
  .contact-list svg { width: 18px; height: 18px; fill: var(--blue); flex: none; }
  .divider {
    position: absolute;
    left: 340px; top: 280px;
    width: 1.5px; height: 66px;
    background: var(--blue);
  }
  .address {
    position: absolute;
    left: 368px; top: 276px;
    font-size: 21px;
    color: var(--white);
    line-height: 1.55;
    font-style: normal;
  }
</style>
</head>
<body>
  <section class="card card-front" aria-label="Business card front">
    <div class="brand"><span class="brand-dot"></span>LOV: Dry Eye</div>
  </section>

  <section class="card card-back" aria-label="Business card back">
    <div class="holder">
      <h1 class="holder-name">Dana Keller</h1>
      <p class="holder-role">CEO/Founder</p>
    </div>
    <div class="brand"><span class="brand-dot"></span>LOV: Dry Eye</div>
    <div class="rule"></div>
    <ul class="contact-list">
      <li>
        <svg viewBox="0 0 24 24" aria-hidden="true"><path d="M6.6 10.8a15.1 15.1 0 0 0 6.6 6.6l2.2-2.2a1 1 0 0 1 1-.25 11.4 11.4 0 0 0 3.6.57 1 1 0 0 1 1 1V20a1 1 0 0 1-1 1A17 17 0 0 1 3 4a1 1 0 0 1 1-1h3.5a1 1 0 0 1 1 1c0 1.25.2 2.450.57 3.6a1 1 0 0 1-.25 1z"/></svg>
        (416) 555 0182
      </li>
      <li>
        <svg viewBox="0 0 24 24" aria-hidden="true"><path d="M2 5h20v14H2zm2 2v.4l8 5 8-5V7zm0 2.8V17h16V9.8l-8 5z"/></svg>
        info@lovdryeye.com
      </li>
      <li>
        <svg viewBox="0 0 24 24" aria-hidden="true"><path d="M12 2a10 10 0 1 0 0 20 10 10 0 0 0 0-20zm6.9 6h-3a15.7 15.7 0 0 0-1.4-3.6A8 8 0 0 1 18.9 8zM12 4c.8 1.2 1.5 2.5 1.9 4h-3.8c.4-1.5 1.1-2.8 1.9-4zM4.3 14a8 8 0 0 1 0-4h3.4a16.5 16.5 0 0 0 0 4zm.8 2h3a15.7 15.7 0 0 0 1.4 3.6A8 8 0 0 1 5.1 16zm3-8h-3a8 8 0 0 1 4.4-3.6A15.7 15.7 0 0 0 8.1 8zM12 20c-.8-1.2-1.5-2.5-1.9-4h3.8c-.4 1.5-1.1 2.8-1.9 4zm2.3-6H9.7a14.7 14.7 0 0 1 0-4h4.6a14.7 14.7 0 0 1 0 4zm.2 5.6a15.7 15.7 0 0 0 1.4-3.6h3a8 8 0 0 1-4.4 3.6zm1.8-5.6a16.5 16.5 0 0 0 0-4h3.4a8 8 0 0 1 0 4z"/></svg>
        www.lovdryeye.com
      </li>
    </ul>
    <div class="divider"></div>
    <address class="address">P.O. Box 3870 Street<br>Ottawa ON K1P 4R2</address>
  </section>
</body>
</html>
```